Flyer Rework for Accountants and Lawyers

Information flyer for accountants and lawyers. Text and flowchart provided. Just need to make it look presentable for print and email. Needs to add logo (AI file provided) and provide graphics. No more than two pages. Our corporate visual identify guidelines are attached (MUST Use). Completed on both AI file and PPTX file.
Target Market(s)
Accountants, Company Directors and Lawyers
Industry/Entity Type
Finance And Accounting
Requirements
Must have
- Our corporate visual identify guidelines are attached (MUST Use)

```html
<!DOCTYPE html>
<html lang="en">
<head>
<meta charset="utf-8">
<title>Fernbridge Advisory – Director Penalty Notices</title>
<link href="https://fonts.googleapis.com/css2?family=Arimo:wght@400;700&display=swap" rel="stylesheet">
<style>
  :root {
    --backdrop: #a7a7a7;
    --paper: #ffffff;
    --paper-tint: #f1f1f1;
    --green: #6cbf4a;
    --green-light: #8fd06a;
    --green-dark: #4f9b34;
    --ink: #2f2f2f;
    --ink-soft: #555555;
    --row-a: #ececec;
    --row-b: #f6f6f6;
  }
  * { box-sizing: border-box; margin: 0; padding: 0; }
  html, body { width: 1200px; height: 1000px; overflow: hidden; }
  body {
    position: relative;
    background: var(--backdrop);
    font-family: "Arimo", Arial, sans-serif;
    color: var(--ink);
  }
  .page {
    position: absolute;
    top: 158px;
    width: 520px;
    height: 670px;
    background: var(--paper);
    overflow: hidden;
  }
  .page--front { left: 75px; }
  .page--back { left: 613px; }

  /* front page */
  .brand {
    position: absolute; left: 30px; top: 30px;
    display: flex; align-items: center; gap: 10px;
  }
  .brand__dot {
    width: 44px; height: 44px; border-radius: 50%;
    background: var(--green);
  }
  .brand__text { font-size: 17px; font-weight: 400; color: var(--ink-soft); line-height: 1.15; }
  .hero {
    position: absolute; left: 0; top: 100px; width: 520px; height: 192px;
  }
  .hero__photo {
    position: absolute; inset: 0;
    background: linear-gradient(100deg, #dde4ea 0%, #c7d3dd 45%, #8ea6bb 75%, #6f8aa1 100%);
  }
  .hero__title {
    position: absolute; left: 43px; top: 22px;
    font-size: 21px; font-weight: 700; line-height: 26px; color: #222;
    letter-spacing: .3px;
  }
  .hero__intro {
    position: absolute; left: 40px; top: 142px; width: 440px;
    font-size: 8.3px; line-height: 10.5px; color: #2c3540;
  }
  .band {
    position: absolute; left: 0; width: 520px;
    background: var(--green);
    font-size: 8.5px; color: #1f3314;
  }
  .band--dpn { top: 302px; height: 19px; padding: 5px 0 0 32px; color: #fff; }
  .body-text {
    position: absolute; left: 31px; width: 460px;
    font-size: 8.2px; line-height: 10.5px; color: var(--ink);
  }
  .body-text--a { top: 338px; }
  .body-text--b { top: 373px; }
  .facts {
    position: absolute; left: 23px; top: 408px; width: 469px;
    border-collapse: collapse; font-size: 8px; line-height: 10px;
  }
  .facts th {
    background: var(--green); color: #1f3314; font-weight: 400;
    height: 19px; text-align: center;
  }
  .facts td { padding: 6px 8px; vertical-align: middle; }
  .facts tr:nth-child(odd) td { background: var(--row-a); }
  .facts tr:nth-child(even) td { background: var(--row-b); }
  .facts td:first-child { width: 104px; color: var(--ink-soft); }
  .facts .indent { display: block; padding-left: 30px; }
  .foot-band {
    position: absolute; left: 0; bottom: 0; width: 520px; height: 26px;
    background: linear-gradient(90deg, var(--green), var(--green-light));
  }

  /* back page */
  .band--tips { top: 28px; height: 24px; padding: 7px 0 0 32px; font-weight: 700; }
  .band--summary { top: 158px; height: 22px; padding: 6px 0 0 32px; font-weight: 700; }
  .tips {
    position: absolute; left: 30px; top: 72px; width: 470px;
    font-size: 8.2px; line-height: 10.3px; padding-left: 12px;
  }
  .tips li { margin-bottom: 4px; }
  .flow {
    position: absolute; left: 0; top: 180px; width: 520px; height: 408px;
    background: var(--paper-tint);
  }
  .flow__lines { position: absolute; left: 0; top: 0; width: 520px; height: 670px; }
  .flow__box {
    position: absolute;
    border: 2px solid var(--green);
    border-radius: 7px;
    background: #fff;
    font-size: 8.3px; line-height: 13.5px;
    padding: 3px 10px;
  }
  .flow__label { position: absolute; font-size: 8.3px; }
  .flow__box ol { list-style: none; }
  .help {
    position: absolute; left: 0; bottom: 0; width: 520px; height: 80px;
    background: linear-gradient(90deg, var(--green-dark), var(--green) 60%, var(--green-light));
    padding: 10px 36px; color: #15240e;
  }
  .help__title { font-size: 8.6px; font-weight: 700; margin-bottom: 5px; }
  .help__text { font-size: 8.2px; line-height: 10px; }
</style>
</head>
<body>

<section class="page page--front">
  <div class="brand">
    <span class="brand__dot"></span>
    <span class="brand__text">FERNBRIDGE ADVISORY<br>Restructuring &amp; Solvency Accountants</span>
  </div>

  <div class="hero">
    <div class="hero__photo" role="img" aria-label="Photo of hands using a tablet showing business bar charts"></div>
    <h1 class="hero__title">INDEPENDENT<br>CONCISE<br>EFFICIENT</h1>
    <p class="hero__intro">Company directors and their advisors need to be aware that non-lodgement of Business Activities Statements (“BAS”) and Superannuation Guarantee Charge (“SCG”) Statements with the ATO may be personally liability for these debts.</p>
  </div>

  <div class="band band--dpn">Director Penalty Notices (“DPN”)</div>

  <p class="body-text body-text--a">The ATO uses DPNs and Garnishee Notices to recovery tax debts and to impose positive obligations on Directors to deal with outstanding PAYG Withholding and the Superannuation Guarantee Charge debts (“Tax Debts”).</p>
  <p class="body-text body-text--b">The DPN regime makes directors of companies who fail to pay Tax Debts personally liable. The key facts of DPN regime are outlined below:</p>

  <table class="facts">
    <tr><th>Facts</th><th>Key facts of a Directors Penalty Notice</th></tr>
    <tr><td>1. Director personal liabilities</td><td>Directors become personally liable for Tax Debts 21 days are the DPN Notice is issued</td></tr>
    <tr><td>2. Automatic liability for unreported and unpaid Tax Debts</td><td>Where a company’s Tax Debts were both unreported and unpaid 3 months after the due date, the directors are automatically personally liable for the Tax Debts.</td></tr>
    <tr><td>3. Avoiding personal liability for directors once they receive a DPN</td><td>Within 21 days of issuing the DPN (which may be received a week or more after issue), a director can avoid personal liability by either:<span class="indent">Paying the Tax Debt</span><span class="indent">Appointing an Administrator to the company</span><span class="indent">Appointing a Liquidator to the company.</span></td></tr>
    <tr><td>4. Effect on new directors</td><td>New directors are liable if outstanding Tax Debts are unpaid 30 days after their appointment as director</td></tr>
    <tr><td>5. Time frames</td><td>ATO can only enforce a DPN after 21 days of giving notice to the director and notice can be given to the company tax agent</td></tr>
  </table>

  <div class="foot-band"></div>
</section>

<section class="page page--back">
  <div class="band band--tips">Tips for directors to limit or avoid personal liability:</div>
  <ol class="tips">
    <li>Always lodge BAS and SGC Statements within 3 months of the due date, even if the liability cannot be paid!</li>
    <li>Act immediately upon receipt of a DPN and consider a payment arrangement with the ATO. This should be considered with care as payments made can be considered as preference payments to the ATO, if a liquidator is appointed. The ATO can make the directors personally liable for the ATO preference claim.</li>
    <li>Seek professional advice from an insolvency practitioner about the options available and possibly save the company through a financial restructure.</li>
  </ol>

  <div class="band band--summary">Summary of the DPN</div>
  <div class="flow"></div>

  <svg class="flow__lines" viewBox="0 0 520 670" aria-hidden="true">
    <defs>
      <marker id="arrowhead" markerWidth="6" markerHeight="6" refX="5" refY="3" orient="auto">
        <path d="M0,0 L6,3 L0,6 Z" fill="#6cbf4a"/>
      </marker>
    </defs>
    <g fill="none" stroke="#6cbf4a" stroke-width="1.5" marker-end="url(#arrowhead)">
      <path d="M268.5 231 V258"/>
      <path d="M197 289 H150 V355"/>
      <path d="M340 289 H380 V355"/>
      <path d="M150 410 V465 H183"/>
      <path d="M356 465 H388 V411"/>
      <path d="M270 502 V525"/>
    </g>
  </svg>

  <div class="flow__box" style="left:197px;top:197px;width:143px;height:34px;">Issued Director’s Penalty<br>Notice By ATO</div>
  <div class="flow__box" style="left:197px;top:259px;width:143px;height:61px;">Business Activity Statement and Superannuation Guarantee Charge lodged within 3 months from due date</div>
  <div class="flow__box" style="left:77px;top:357px;width:149px;height:53px;">Director not personally liable yet.<br>(Have options)<br>[RIGHTS PRESERVED]</div>
  <div class="flow__box" style="left:320px;top:357px;width:134px;height:53px;padding-top:9px;">Director Automatically<br>personally liable</div>
  <div class="flow__box" style="left:185px;top:437px;width:171px;height:65px;">
    If Directors act within 21 days and:
    <ol><li>1. Wind up Company voluntarily; or</li><li>2. Appoint Voluntary Administrator; or</li><li>3. Pay debt in full</li></ol>
  </div>
  <div class="flow__box" style="left:185px;top:527px;width:171px;height:36px;text-align:center;">Director not personally liable but the company is still insolvent.</div>

  <span class="flow__label" style="left:136px;top:318px;">No</span>
  <span class="flow__label" style="left:385px;top:318px;">Yes</span>
  <span class="flow__label" style="left:390px;top:434px;">No</span>
  <span class="flow__label" style="left:274px;top:506px;">Yes</span>

  <div class="help">
    <p class="help__title">How Fernbridge Advisory can help?</p>
    <p class="help__text">Fernbridge Advisory is a firm that specialises in insolvency and restructuring, we are here to assist your clients who experiencing financial difficulties with straight forward solutions in simple to understand terms. The initial consultation is free, strictly confidential and without obligation. Please call <b>(02) 5550 1234</b> to speak to one of our solvency specialist or email <b>info@fernbridgeadvisory.example</b>.</p>
  </div>
</section>

</body>
</html>
```